Meridel Haulage - Website

A clean, not cluttered informative website for our business. We specialize in the transportation of radioactive materials across North America. The site is mostly for information about our company and will not be used to attract business but will be used to attract employee's mainly drivers. Driver's are very hard to find in our area. One of the pages needs to be a job's posting page with an apply now button. Either an application can be filled out there or a resume can be uploaded which ever functionality works better. I would like a website that I can easily edit, ability to change text and photos.

Number of Pages Required

5+ page

Colors

Designer to choose colors to be used in the design.

Requirements
Must have
• Home - About - Services - Jobs - Contact pages
• A way prospective employee's can apply or upload their resume to be emailed to me
• Very clean apperance
Should not have
• I don't want it to be busy

```html
<!DOCTYPE html>
<html lang="en">
<head>
<meta charset="utf-8">
<title>Meridel Haulage</title>
<link rel="stylesheet" href="https://fonts.googleapis.com/css2?family=Open+Sans:ital,wght@0,300;0,400;0,600;0,700;1,400;1,600&display=swap">
<style>
:root{
  --ink:#111111;
  --night:#1c1c1c;
  --charcoal:#2a2827;
  --social-band:#2b2b2b;
  --orange:#f7941d;
  --orange-deep:#e8562a;
  --blue:#1a6fb5;
  --text-dark:#333333;
  --text-mute:#8a8a8a;
  --white:#ffffff;
  --field:#ffffff;
  --field-grey:#d9d9d9;
  --frame:#8a4a3a;
}
*{box-sizing:border-box;margin:0;padding:0}
html,body{width:1200px;height:2375px;overflow:hidden}
body{font-family:"Open Sans",Arial,sans-serif;background:var(--white);color:var(--text-dark);position:relative}
.abs{position:absolute}

/* header */
.site-header{left:0;top:0;width:1200px;height:137px;background:var(--ink)}
.brand{left:44px;top:44px;display:flex;align-items:center;gap:14px;color:#cfcfcf;font-size:44px;font-weight:700;letter-spacing:1px;line-height:1}
.brand-mark{width:22px;height:22px;background:#cfcfcf;border-radius:50%}
.top-contact{top:12px;display:flex;align-items:center;gap:8px;color:var(--white)}
.top-contact small{display:block;font-size:9px;font-style:italic;line-height:1.1}
.top-contact span{font-size:12px;line-height:1.1}
.top-icon{width:20px;height:20px;background:var(--white);border-radius:3px;display:flex;align-items:center;justify-content:center}
.main-nav{left:630px;top:92px;display:flex;font-size:13px;color:var(--white)}
.main-nav a{color:var(--white);text-decoration:none;padding:0 16px;border-left:1px solid #bbb;line-height:14px}
.main-nav a:first-child{border-left:none;padding-left:0}

/* hero */
.hero-photo{left:0;top:137px;width:1200px;height:429px;background:linear-gradient(180deg,#b8b6b2 0%,#8d8a86 45%,#5f5d5a 75%,#3f3e3c 100%)}
.contact-panel{left:888px;top:167px;width:255px;height:365px;background:var(--night)}
.contact-panel h2{height:59px;background:var(--orange);color:var(--white);font-size:23px;font-weight:700;text-align:center;line-height:59px}
.contact-panel p{color:var(--white);font-size:11px;text-align:center;padding:14px 22px 0;line-height:1.5}
.field{display:block;width:208px;height:35px;margin:6px auto 0;background:var(--field);font-size:11px;color:#333;padding:10px 8px}
.field.tall{height:64px}
.btn-submit{display:block;width:208px;height:34px;margin:8px auto 0;background:var(--orange);color:var(--white);font-size:13px;text-align:center;line-height:34px;font-weight:600}
.slider-dots{left:566px;top:530px;display:flex;gap:6px}
.slider-dots i{width:17px;height:17px;border-radius:50%;border:2px solid var(--white);background:#777}
.slider-dots i:first-child{background:var(--white)}

/* intro */
.intro{z-index:2}
.intro h2{font-size:33px;font-weight:400;color:var(--text-dark);letter-spacing:.5px;line-height:45px}
.intro h2 b{font-weight:700}
.intro p{font-size:11px;line-height:15.5px;margin-top:12px;color:#222}
.intro ul{list-style:none;margin-top:10px}
.intro li{font-size:11px;line-height:15.5px;padding-left:16px;position:relative;margin-bottom:6px}
.intro li::before{content:"";position:absolute;left:0;top:3px;border-left:8px solid #d9382a;border-top:5px solid transparent;border-bottom:5px solid transparent}

/* benefits */
.road-photo{left:0;top:830px;width:1200px;height:566px;background:linear-gradient(180deg,#f4f5f7 0%,#dfe3e8 22%,#b9b3a9 48%,#8e8679 68%,#5f5a54 100%)}
.feature-name{left:0;top:858px;width:1200px;text-align:center;color:var(--blue);font-size:50px;font-weight:700;letter-spacing:1px}
.section-title-dark{left:0;top:1070px;width:1200px;text-align:center;font-size:38px;font-weight:700;color:#111}
.benefit{top:1148px;width:250px;height:192px;background:var(--white);text-align:center;box-shadow:6px 6px 0 rgba(0,0,0,.55)}
.benefit svg{margin-top:20px}
.benefit h3{font-size:20px;font-weight:400;font-style:italic;color:var(--orange-deep);margin-top:10px}
.benefit h3 b{font-weight:400;text-transform:uppercase}
.benefit p{font-size:9.5px;line-height:1.6;color:#444;padding:4px 22px 0}
.benefit a{display:block;font-size:12px;color:#222;text-decoration:none;margin-top:6px}

/* jobs */
.jobs{left:0;top:1396px;width:1200px;height:485px;background:var(--charcoal);border-top:2px solid #cfcfcf}
.jobs h2{position:absolute;left:0;top:30px;width:1200px;text-align:center;color:#c9c9c9;font-size:32px;font-weight:400}
.jobs .lead{position:absolute;left:320px;top:80px;width:560px;text-align:center;color:var(--text-mute);font-size:10.5px;line-height:1.6}
.btn-resume{position:absolute;left:543px;top:131px;width:143px;height:41px;background:var(--orange);border:2px solid #f3c27a;border-radius:3px;color:var(--white);font-size:15px;text-align:center;line-height:37px;text-decoration:none}
.specialities{position:absolute;left:111px;top:203px;width:450px}
.specialities .kicker{color:var(--orange);font-size:25px;font-weight:400}
.specialities h3{color:#bdbdbd;font-size:22px;font-weight:400;margin-top:-2px}
.specialities p{color:var(--text-mute);font-size:11px;line-height:1.5;margin-top:10px}
.specialities ul{list-style:none;margin-top:14px}
.specialities li{color:var(--text-mute);font-size:10.5px;line-height:1.5;padding-left:24px;position:relative;margin-bottom:14px}
.specialities li::before{content:"";position:absolute;left:2px;top:3px;border-left:9px solid var(--orange);border-top:5px solid transparent;border-bottom:5px solid transparent}
.testimonial{position:absolute;left:698px;top:207px;width:374px;height:215px;border:1px solid var(--frame);border-radius:3px}
.avatar{position:absolute;left:47px;top:28px;width:48px;height:48px;border-radius:50%;background:#c7b39d;border:2px solid var(--white)}
.testimonial h4{position:absolute;left:110px;top:30px;color:#cfcfcf;font-size:18px;font-weight:400}
.testimonial time{position:absolute;left:110px;top:56px;color:#9a9a9a;font-size:10px;font-style:italic}
.testimonial blockquote{position:absolute;left:24px;top:86px;width:330px;color:var(--text-mute);font-size:10.5px;line-height:1.45;text-align:justify}
.testimonial blockquote::before{content:"\201C";color:var(--orange);font-size:24px;font-weight:700;line-height:0;vertical-align:-8px;margin-right:4px}
.testimonial .more{position:absolute;left:24px;top:164px;color:#d0d0d0;font-size:10px;font-style:italic;display:flex;align-items:center;gap:10px}

/* footer */
.site-footer{left:0;top:1881px;width:1200px;height:331px;background:var(--ink);border-top:2px solid #cfcfcf}
.site-footer h2{position:absolute;left:0;top:35px;width:1200px;text-align:center;color:var(--white);font-size:32px;font-weight:400}
.site-footer h2 b{font-weight:600}
.foot-col{position:absolute;top:108px}
.foot-col h3{font-size:18px;font-style:italic;font-weight:400;color:var(--white);width:157px;border-bottom:1px solid #888;padding-bottom:2px;margin-bottom:10px}
.foot-col li{list-style:none;color:var(--white);font-size:16px;line-height:30px;display:flex;align-items:center;gap:10px}
.foot-col li.muted{color:#aaa}
.foot-col .chev{font-size:16px}
.foot-col .field{margin:6px 0 0;width:212px;height:35px;background:var(--field-grey)}
.foot-col .btn-submit{margin:6px 0 0;width:212px;height:35px;line-height:35px}
.social-band{left:0;top:2212px;width:1200px;height:98px;background:var(--social-band)}
.social{position:absolute;top:18px;width:65px;height:65px;border-radius:50%}
.copyright{left:0;top:2310px;width:1200px;height:65px;background:var(--ink);color:var(--white);font-size:15px;text-align:center;line-height:65px}
</style>
</head>
<body>

<header class="site-header abs">
  <div class="brand abs"><span class="brand-mark"></span>Meridel Haulage</div>
  <div class="top-contact abs" style="left:785px">
    <div class="top-icon"><svg width="12" height="12" viewBox="0 0 24 24"><path d="M6 2l4 4-2 3c1 3 4 6 7 7l3-2 4 4-3 4C10 22 2 14 2 5z" fill="#111"/></svg></div>
    <div><small>Call Us</small><span>180-000-0000</span></div>
  </div>
  <div class="top-contact abs" style="left:910px">
    <div class="top-icon"><svg width="12" height="12" viewBox="0 0 24 24"><rect x="4" y="2" width="16" height="20" fill="none" stroke="#111" stroke-width="2"/><path d="M8 8h8M8 12h8M8 16h5" stroke="#111" stroke-width="2"/></svg></div>
    <div><small>Post Your Resume</small><span>recruitment@meridelhaulage.com</span></div>
  </div>
  <nav class="main-nav abs">
    <a href="#">HOME</a><a href="#">ABOUT US</a><a href="#">OUR SERVICES</a><a href="#">JOBS</a><a href="#">CONTACT US</a>
  </nav>
</header>

<div class="hero-photo abs" role="img" aria-label="Photo of a grey semi truck hauling cylindrical containers on a flatbed trailer"></div>
<form class="contact-panel abs">
  <h2>GET IN TOUCH</h2>
  <p>Lorem Ipsum is simply dummy text of the printing and typesetting industry.</p>
  <span class="field">Name</span>
  <span class="field">Email</span>
  <span class="field">Ph Number</span>
  <span class="field tall">Message</span>
  <span class="btn-submit">SUBMIT</span>
</form>
<div class="slider-dots abs"><i></i><i></i><i></i></div>

<div class="road-photo abs" role="img" aria-label="Photo of a straight desert highway leading toward misty mountains"></div>

<section class="intro abs" style="left:112px;top:618px;width:372px">
  <h2>WHO <b>WE ARE?</b></h2>
  <p>Lorem Ipsum is simply dummy text of the printing and typesetting industry. Lorem Ipsum has been the industry's standard dummy text ever since the 1500s, when an unknown printer took a galley of type and scrambled it to make a type specimen book.Lorem Ipsum is simply dummy text of the printing and typesetting industry. Lorem Ipsum has been the industry's standard dummy text ever since the 1500s, when an unknown printer took a galley of type and scrambled it to make a type specimen book.</p>
</section>
<section class="intro abs" style="left:716px;top:618px;width:400px">
  <h2>SERVICES <b>WE PROVIDE</b></h2>
  <p>Lorem Ipsum is simply dummy text of the printing and typesetting industry. Lorem Ipsum has been the industry's standard dummy text.</p>
  <ul>
    <li>Lorem Ipsum is simply dummy text of the printing<br>and typesetting industry.</li>
    <li>Lorem Ipsum is simply dummy text.</li>
    <li>Lorem Ipsum is simply dummy text.</li>
  </ul>
</section>

<div class="feature-name abs">Meridel Haulage</div>
<h2 class="section-title-dark abs">WHAT BENEFITS YOU GET?</h2>

<article class="benefit abs" style="left:63px">
  <svg width="56" height="56" viewBox="0 0 56 56"><rect x="5" y="9" width="46" height="42" rx="3" fill="none" stroke="#1a6fb5" stroke-width="4"/><rect x="5" y="9" width="46" height="10" fill="#1a6fb5"/><path d="M16 4v10M40 4v10" stroke="#1a6fb5" stroke-width="4"/><g fill="#1a6fb5"><rect x="12" y="24" width="8" height="7"/><rect x="24" y="24" width="8" height="7"/><rect x="36" y="24" width="8" height="7"/><rect x="12" y="36" width="8" height="7"/><rect x="24" y="36" width="8" height="7"/><rect x="36" y="36" width="8" height="7"/></g></svg>
  <h3><b>easy</b> booking</h3>
  <p>It is a long established fact that a reader will be distracted by the readable content.</p>
  <a href="#">View more ›</a>
</article>
<article class="benefit abs" style="left:333px">
  <svg width="96" height="56" viewBox="0 0 96 56"><rect x="4" y="6" width="56" height="36" fill="#1a6fb5"/><path d="M62 16h18l12 14v12H62z" fill="#1a6fb5"/><circle cx="20" cy="46" r="8" fill="#1a6fb5" stroke="#fff" stroke-width="3"/><circle cx="76" cy="46" r="8" fill="#1a6fb5" stroke="#fff" stroke-width="3"/></svg>
  <h3><b>fast</b> delivery</h3>
  <p>It is a long established fact that a reader will be distracted by the readable content.</p>
  <a href="#">View more ›</a>
</article>
<article class="benefit abs" style="left:604px">
  <svg width="56" height="56" viewBox="0 0 56 56"><circle cx="28" cy="28" r="24" fill="#1a6fb5"/><path d="M16 29l8 8 16-17" fill="none" stroke="#fff" stroke-width="5"/></svg>
  <h3><b>hassle</b> free</h3>
  <p>It is a long established fact that a reader will be distracted by the readable content</p>
  <a href="#">View more ›</a>
</article>
<article class="benefit abs" style="left:876px">
  <svg width="56" height="56" viewBox="0 0 56 56"><circle cx="28" cy="22" r="16" fill="#1a6fb5"/><circle cx="28" cy="22" r="7" fill="#fff"/><rect x="18" y="40" width="20" height="14" rx="3" fill="#1a6fb5"/></svg>
  <h3><b>affordable</b> price</h3>
  <p>It is a long established fact that a reader will be distracted by the readable content</p>
  <a href="#">View more ›</a>
</article>

<section class="jobs abs">
  <h2>JOB OPPORTUNITIES</h2>
  <p class="lead">Lorem Ipsum is simply dummy text of the printing and typesetting industry. Lorem Ipsum has been the industry's standard dummy text ever since the 1500s, when an unknown printer took a galley.</p>
  <a class="btn-resume" href="#">Post Your Resume</a>
  <div class="specialities">
    <div class="kicker">LOOK AT</div>
    <h3>OUR JOB SPECIALITIES</h3>
    <p>Lorem Ipsum is simply dummy text of the printing and typesetting industry. Lorem Ipsum has been the industry's standard dummy text ever since the 1500s, when an unknown printer took a galley.</p>
    <ul>
      <li>Lorem Ipsum is simply dummy text of the printing and typesetting industry. Lorem Ipsum has been the industry's standard dummy text.</li>
      <li>Lorem Ipsum is simply dummy text of the printing and typesetting industry. Lorem Ipsum has been the industry's standard dummy text.</li>
    </ul>
  </div>
  <div class="testimonial">
    <div class="avatar" role="img" aria-label="Portrait of the reviewer"></div>
    <h4>Dana Whitlow</h4>
    <time>monday 15 Dec2015</time>
    <blockquote>Lorem Ipsum is simply dummy text of the printing and typesetting industry. Lorem Ipsum has been the industry's standard dummy text.Lorem Ipsum has been the industry's standard dummy text.</blockquote>
    <div class="more">VIEW ALL TESTIMONIALS <svg width="18" height="14" viewBox="0 0 18 14"><path d="M0 7h12M9 1l7 6-7 6" fill="none" stroke="#fff" stroke-width="3"/></svg></div>
  </div>
</section>

<footer class="site-footer abs">
  <h2>CONNECT <b>WITH US</b></h2>
  <div class="foot-col" style="left:133px">
    <h3>SITELINK</h3>
    <ul><li class="muted"><span class="chev">›</span>Home</li><li><span class="chev">›</span>About Us</li><li><span class="chev">›</span>Our Services</li><li><span class="chev">›</span>Jobs</li><li><span class="chev">›</span>Contact Us</li></ul>
  </div>
  <div class="foot-col" style="left:372px">
    <h3>COMPANY RULES</h3>
    <ul><li><span class="chev">›</span>Company terms</li><li><span class="chev">›</span>Rules and regulation</li><li><span class="chev">›</span>Privacy policy</li><li><span class="chev">›</span>Help</li></ul>
  </div>
  <div class="foot-col" style="left:640px">
    <h3>CONATCT US</h3>
    <ul>
      <li><svg width="14" height="14" viewBox="0 0 24 24"><path d="M6 2l4 4-2 3c1 3 4 6 7 7l3-2 4 4-3 4C10 22 2 14 2 5z" fill="#fff"/></svg>180-000-0000</li>
      <li><svg width="16" height="14" viewBox="0 0 24 20"><rect x="2" y="7" width="20" height="12" fill="#fff"/><rect x="6" y="1" width="12" height="6" fill="#fff"/></svg>180-000-0001</li>
    </ul>
  </div>
  <form class="foot-col" style="left:865px">
    <h3>GET A QUOTE</h3>
    <span class="field">Name</span>
    <span class="field">Email</span>
    <span class="field">Ph Number</span>
    <span class="btn-submit">SUBMIT</span>
  </form>
</footer>

<div class="social-band abs">
  <span class="social" style="left:437px;background:#3b5a9a" aria-label="Social profile"></span>
  <span class="social" style="left:516px;background:#55c5ef" aria-label="Social profile"></span>
  <span class="social" style="left:596px;background:#d23a2a" aria-label="Social profile"></span>
  <span class="social" style="left:676px;background:#1c84b5" aria-label="Social profile"></span>
</div>
<div class="copyright abs">© 2019 website. All rights reserved.</div>

</body>
</html>
```